Word Press Website design

Harborlight Studio is a Website design, SEO, Social Networking and app development company. We would like to see what you can do to create a new, relevant and exciting design for us. This is our first project for Pixel Meadow so we thought we would test drive this site.  We would like to leave it up to your creative interpretation of the new design, but you can checkout our old design at www.harborlightstudiohub.example
We are always looking for new talent for future projects. Wow us with your designs and there will be future work for you.

Target Market(s)
Our target customers are medium sized businesses of all vertical markets.
Industry/Entity Type
Internet
Font styles to use
Requirements
Must have
- Easy to navigate, HTML 5 sliders, modern
Nice to have
- Bring your graphic talents with an outside of the box design that will standout to prospective clients.

```html
<!DOCTYPE html>
<html lang="en">
<head>
<meta charset="utf-8">
<title>Harborlight Studio</title>
<link rel="stylesheet" href="https://fonts.googleapis.com/css2?family=Raleway:wght@400;500&family=Open+Sans:ital,wght@0,400;0,600;1,400&display=swap">
<style>
:root{
  --ink:#2f2f2f;
  --muted:#8a8a8a;
  --brand:#4d4a7e;
  --hero-top:#8080a9;
  --hero-bottom:#4b487c;
  --band:#f7f7f7;
  --line:#e6e6e6;
  --footer:#2b2b2b;
  --footer-text:#d6d6d6;
  --accent:#e07b1a;
}
*{margin:0;padding:0;box-sizing:border-box}
html,body{width:785px;height:1200px;overflow:hidden;background:#fff}
body{font-family:"Open Sans",Arial,sans-serif;color:var(--ink);position:relative}
.abs{position:absolute}

/* header */
.site-header{left:0;top:0;width:785px;height:58px;background:#fff}
.brand{left:130px;top:8px;display:flex;align-items:center;gap:6px}
.brand-mark{width:16px;height:16px;background:var(--ink)}
.brand-name{font-family:"Raleway",sans-serif;font-weight:500;font-size:15px;color:var(--ink)}
.phone{left:582px;top:9px;font-size:9.5px;color:#222;display:flex;align-items:center;gap:3px}
.main-nav{left:338px;top:32px;display:flex;gap:16.5px;font-family:"Raleway",sans-serif;font-size:7.6px;color:#444}

/* hero */
.hero{left:0;top:58px;width:785px;height:315px;background:linear-gradient(var(--hero-top),var(--hero-bottom));overflow:hidden}
.hero h1{position:absolute;left:0;width:785px;top:26px;text-align:center;font-family:"Raleway",sans-serif;font-weight:400;font-size:20px;color:#fff}
.hero p{position:absolute;left:190px;width:405px;top:53px;text-align:center;font-family:"Raleway",sans-serif;font-size:9.2px;line-height:16px;color:#f0f0f6}
.slide-frame{left:224px;top:98px;width:335px;height:217px;border-radius:3px 3px 0 0;overflow:hidden;background:#2a2a2a}
.slide-bar{height:20px;background:linear-gradient(#f2f2f2,#cfcfcf)}
.slide-shot{position:absolute;left:2px;top:20px;width:331px;height:197px;background:linear-gradient(#303030 0%,#1c1c1c 60%,#bdbdbd 60%,#8f8f8f 76%,#2b2b2b 76%)}
.slider-arrow{top:215px}

/* about */
.about h2,.clients h2{font-family:"Raleway",sans-serif;font-weight:400;color:var(--brand);text-align:center}
.about{left:0;top:402px;width:785px}
.about h2{font-size:17px}
.about p{width:485px;margin:8px auto 0;font-size:5.6px;line-height:10.4px;text-align:center;color:#555}
.about p + p{margin-top:3px}

/* services */
.services{left:0;top:529px;width:785px;height:254px;background:var(--band);border-top:1px solid var(--line);border-bottom:1px solid var(--line)}
.services-tab{left:300px;top:-1px;width:190px;height:34px;background:#eeeeee;clip-path:polygon(0 0,100% 0,92% 100%,8% 100%);text-align:center;font-family:"Raleway",sans-serif;font-size:13.5px;line-height:40px;color:#3a3a3a}
.service{width:178px;height:60px}
.service-icon{position:absolute;left:0;top:0;width:49px;height:49px;border-radius:50%;background:#fff;border:1px solid #e8e8e8;display:flex;align-items:center;justify-content:center}
.service-body{position:absolute;left:54px;top:0}
.service h3{font-family:"Raleway",sans-serif;font-weight:500;font-size:9.6px;color:#333}
.service p{font-size:5.7px;line-height:10.3px;color:#999;width:120px;margin-top:2px}
.service a{display:block;font-size:5.8px;color:var(--brand);margin-top:2px;text-decoration:none}

/* testimonials */
.clients{left:0;top:822px;width:785px}
.clients h2{font-size:14px}
.client-name{left:0;width:785px;top:866px;display:flex;justify-content:center;align-items:center;gap:6px}
.client-dot{width:18px;height:18px;border-radius:50%;background:#2f6ea8}
.client-label{font-family:"Open Sans",sans-serif;font-weight:600;font-size:13px;color:#1f5b8f}
.quote{left:215px;width:360px;top:896px;text-align:center;font-style:italic;font-size:6.8px;line-height:11.8px;color:#999}
.byline{left:0;width:785px;top:932px;text-align:center;font-size:6.6px;color:#333}

/* footer */
.site-footer{left:0;top:1006px;width:785px;height:194px;background:var(--footer)}
.footer-col{top:24px}
.footer-col h4{font-family:"Raleway",sans-serif;font-weight:400;font-size:9.2px;color:#eee;margin-bottom:4px}
.footer-col li{list-style:none;font-size:6.2px;line-height:14.4px;color:var(--footer-text)}
.footer-rule{width:2px;top:22px;height:96px;background:linear-gradient(rgba(0,0,0,0),rgba(0,0,0,.45),rgba(0,0,0,0))}
.socials{display:flex;gap:9px;margin-top:8px}
.socials span{width:11px;height:11px;border-radius:50%;background:#9a9a9a}
.footer-bottom{left:128px;width:527px;top:153px;border-top:1px solid #3c3c3c;padding-top:12px;font-size:5.8px;color:#777}
</style>
</head>
<body>

<header class="abs site-header">
  <div class="abs brand"><span class="brand-mark"></span><span class="brand-name">Harborlight Studio</span></div>
  <div class="abs phone">
    <svg width="9" height="9" viewBox="0 0 24 24"><path fill="var(--accent)" d="M6.6 10.8a15 15 0 0 0 6.6 6.6l2.2-2.2c.3-.3.7-.4 1-.2 1.1.4 2.3.6 3.6.6.6 0 1 .4 1 1V20c0 .6-.4 1-1 1A17 17 0 0 1 3 4c0-.6.4-1 1-1h3.5c.6 0 1 .4 1 1 0 1.3.2 2.5.6 3.6.1.3 0 .7-.2 1z"/></svg>
    555.014.2290
  </div>
  <nav class="abs main-nav"><span>About Us</span><span>Services</span><span>Portfolio</span><span>Case studies</span><span>Testimonials</span><span>Contact Us</span></nav>
</header>

<section class="abs hero">
  <h1>We Provide Web Designing &amp; SEO Services</h1>
  <p>Lorem ipsum dolor sit amet consectetuer adipiscing elit cursus Morbi ut mi Nullam enim leo egestas id condimentum at laoreet mattis</p>
  <div class="abs slide-frame">
    <div class="slide-bar"></div>
    <div class="slide-shot" role="img" aria-label="Slider preview of a dark website template shown in a browser window"></div>
  </div>
  <svg class="abs slider-arrow" style="left:128px;top:157px" width="18" height="42"><path d="M16 1 2 21l14 20" fill="none" stroke="#d8d8ea" stroke-width="1.2"/></svg>
  <svg class="abs slider-arrow" style="left:640px;top:157px" width="18" height="42"><path d="M2 1l14 20L2 41" fill="none" stroke="#d8d8ea" stroke-width="1.2"/></svg>
</section>

<section class="abs about">
  <h2>About Harborlight Studio Inc.</h2>
  <p>Harborlight Studio has been developing custom Websites in Kansas City since 1998. We build living, breathing, dynamic Website designs to meet the needs of diverse businesses. Website designers are a dime a dozen. Why pay for what you can get for FREE? Because your time is better spent running your business. Your time and money is valuable, and we can maximize both. Let Harborlight Studio create your next Website because your image matters</p>
  <p>Harborlight Studio creates Websites that will wow your customers and blow away your competition. While browsing the Web, do you ever say "This company looks legitimate?" Your customers make the same snap judgments. We build trustworthy and professional custom Website designs that Kansas City businesses rely upon.</p>
</section>

<section class="abs services">
  <div class="abs services-tab">Services Provides</div>

  <div class="abs service" style="left:128px;top:65px">
    <div class="service-icon"><svg width="22" height="20" viewBox="0 0 24 22"><rect x="1" y="1" width="22" height="15" rx="1.5" fill="var(--brand)"/><rect x="3.5" y="3.5" width="17" height="10" fill="#fff"/><rect x="9" y="16" width="6" height="3" fill="var(--brand)"/><rect x="6" y="19" width="12" height="2" fill="var(--brand)"/></svg></div>
    <div class="service-body"><h3>Web Design</h3><p>Morbi diam mauris viverra in gravida eu mattis in ante Morbi eget arcu Morbi porta libero id ullamcorper nonummy nib</p><a>Learn More</a></div>
  </div>
  <div class="abs service" style="left:308px;top:65px">
    <div class="service-icon"><svg width="18" height="20" viewBox="0 0 18 20"><g fill="var(--brand)"><ellipse cx="9" cy="3.5" rx="8" ry="3"/><path d="M1 6c0 2 4 3 8 3s8-1 8-3v3.5c0 1.7-3.6 3-8 3s-8-1.3-8-3z"/><path d="M1 11.5c0 2 4 3 8 3s8-1 8-3V15c0 1.7-3.6 3-8 3s-8-1.3-8-3z"/></g></svg></div>
    <div class="service-body"><h3>Hosting Service</h3><p>Morbi diam mauris viverra in gravida eu mattis in ante Morbi eget arcu Morbi porta libero id ullamcorper nonummy nib</p><a>Learn More</a></div>
  </div>
  <div class="abs service" style="left:488px;top:65px">
    <div class="service-icon"><svg width="22" height="20" viewBox="0 0 24 22"><path d="M1 2h4l3 11h12l3-8H7" fill="none" stroke="var(--brand)" stroke-width="2.4"/><path d="M7 5h16l-3 8H8z" fill="var(--brand)"/><circle cx="9.5" cy="18" r="2" fill="var(--brand)"/><circle cx="18" cy="18" r="2" fill="var(--brand)"/></svg></div>
    <div class="service-body"><h3>eCommerce</h3><p>Morbi diam mauris viverra in gravida eu mattis in ante Morbi eget arcu Morbi porta libero id ullamcorper nonummy nib</p><a>Learn More</a></div>
  </div>

  <div class="abs service" style="left:129px;top:157px">
    <div class="service-icon"><svg width="26" height="18" viewBox="0 0 26 18"><path d="M8 3 2 9l6 6M18 3l6 6-6 6M15 1l-4 16" fill="none" stroke="var(--brand)" stroke-width="2"/></svg></div>
    <div class="service-body"><h3>Programming</h3><p>Morbi diam mauris viverra in gravida eu mattis in ante Morbi eget arcu Morbi porta libero id ullamcorper nonummy nib</p><a>Learn More</a></div>
  </div>
  <div class="abs service" style="left:309px;top:157px">
    <div class="service-icon"><svg width="22" height="18" viewBox="0 0 22 18"><path d="M1 1v16h20" fill="none" stroke="var(--brand)" stroke-width="2"/><path d="M4 13l5-5 3 3 6-7" fill="none" stroke="var(--brand)" stroke-width="2.2"/><path d="M14 3h5v5z" fill="var(--brand)"/></svg></div>
    <div class="service-body"><h3>SEO</h3><p>Morbi diam mauris viverra in gravida eu mattis in ante Morbi eget arcu Morbi porta libero id ullamcorper nonummy nib</p><a>Learn More</a></div>
  </div>
  <div class="abs service" style="left:489px;top:157px">
    <div class="service-icon"><svg width="22" height="18" viewBox="0 0 22 18"><path d="M2 4h5l2-3h4l2 3h5v13H2z" fill="var(--brand)"/><circle cx="11" cy="10" r="4.3" fill="#fff"/><circle cx="11" cy="10" r="2.6" fill="var(--brand)"/></svg></div>
    <div class="service-body"><h3>Photography Service</h3><p>Morbi diam mauris viverra in gravida eu mattis in ante Morbi eget arcu Morbi porta libero id ullamcorper nonummy nib</p><a>Learn More</a></div>
  </div>
</section>

<section class="abs clients"><h2>WHAT OUR CLIENT SAY</h2></section>
<div class="abs client-name"><span class="client-dot"></span><span class="client-label">Northgate Partners</span></div>
<svg class="abs" style="left:171px;top:880px" width="16" height="38"><path d="M15 1 2 19l13 18" fill="none" stroke="#999" stroke-width="1"/></svg>
<svg class="abs" style="left:602px;top:880px" width="16" height="38"><path d="M1 1l13 18L1 37" fill="none" stroke="#999" stroke-width="1"/></svg>
<p class="abs quote"><span style="font-style:normal;font-size:12px;color:#555">&ldquo;</span> Morbi diam mauris viverra in gravida eu mattis in ante Morbi eget arcu Morbi porta libero id ullamcorper nonummy nibh ligula pulvinar metus eget consectetuer augue nisi quis lacus Ut ac mi quis lacus mollis aliquam Curabitur iaculis tempus eros Curabitur vel mi sit amet Mauris vel lacus vitae felis <span style="font-style:normal;font-size:12px;color:#555">&rdquo;</span></p>
<p class="abs byline">By Ridgeline Tackle Co., City Location</p>

<footer class="abs site-footer">
  <div class="abs footer-col" style="left:133px"><h4>Company</h4><ul><li>About Us</li><li>What We Do</li><li>Solutions</li><li>Hire Us</li></ul></div>
  <div class="abs footer-rule" style="left:200px"></div>
  <div class="abs footer-col" style="left:227px"><h4>Services</h4><ul><li>SEO</li><li>Web Design</li><li>Ecommerce</li><li>Hosting</li><li>Programming</li></ul></div>
  <div class="abs footer-rule" style="left:311px"></div>
  <div class="abs footer-col" style="left:342px"><h4>Resources</h4><ul><li>Testimonials</li><li>Career</li><li>Case studies</li><li>Portoflio</li></ul></div>
  <div class="abs footer-rule" style="left:410px"></div>
  <div class="abs footer-col" style="left:459px"><h4>Support</h4><ul><li>Support</li><li>Term of Use</li><li>Contac Us</li></ul></div>
  <div class="abs footer-rule" style="left:526px"></div>
  <div class="abs footer-col" style="left:562px"><h4>Get in Touch</h4><ul><li>Connect with us on social sites.</li></ul>
    <div class="socials"><span></span><span></span><span></span><span></span></div>
  </div>
  <div class="abs footer-bottom">© 2014 Company Name  All right reserved  Term of Use</div>
</footer>

</body>
</html>
```